Zielgruppe
Medtech Company
mTOR ins ein sehr wichtiger Wachstumsregulator in menschlichen Zellen. Wenn damit etwas nicht richtig funktioniert (wenn mTOR zu aktiv ist) wachsen Zellen zu schnell und können Tumore bilden. Velunor entwickelt neue pharmazeutische Medikamente zum bremsen des mTOR-Signalwegs. mTOR arbeitet in der Zelle in zwei Formen: 'mTOR Complex 1' und 'mTOR Complex 2'. Unsere Medikamente können 'mTOR Complex 1' und 'mTOR Complex 2' unterscheiden, und werden in der Zukunft für die Behandlung der genetischen Krankheit Tuberöse Sklerose und verschiedenen Krebsarten eingesetzt.
Aufgabenstellung
Konventionelle Medikamente hemmen die Aktivität von mTOR. Bei unserem Ansatz können wir viel gezielter entweder selektiv 'mTOR complex 1' (in grün) oder 'mTOR complex 2' (in orange) hemmen. Dadurch werde unsere Medikamente besser wirken und weniger Nebenwirkungen haben. Die Unterscheidung von 'mTOR complex 1' und 'mTOR complex 2' zieht sich durch die gesamten Folien durch. Visuell erreichen wir das durch die beiden verschiedenen Farben grün und orange. Als neutrale Farbe verwenden wir blau, und als Warnfarbe rot (die Hex-Codes sind angehängt. Schrift is Helvetica Neue.
Main Colors:
Blue 36537D
Light blue E9F4FF
Gray F0F1F2
Red (bad) F43D38
Light red FFEEEE
Programs / Application area:
mTOR complex 1
Green 45A052
Light Green EDFCEE
mTOR complex 2
Orange BCB704
Light Orange FFEEE6

```html
<!DOCTYPE html>
<html lang="en">
<head>
<meta charset="utf-8">
<title>Velunor – mTOR inhibition</title>
<link href="https://fonts.googleapis.com/css2?family=Arimo:wght@400;700&display=swap" rel="stylesheet">
<style>
:root{
  --blue:#36537D;
  --light-blue:#E9F4FF;
  --gray:#F0F1F2;
  --red:#F43D38;
  --green:#45A052;
  --light-green:#E8FBEA;
  --orange:#DF7A3F;
  --light-orange:#FFEEE6;
  --white:#FFFFFF;
  --text:#3C4A5C;
}
*{box-sizing:border-box;margin:0;padding:0}
html,body{width:1200px;height:3348px;overflow:hidden}
body{font-family:"Arimo",Helvetica,Arial,sans-serif;color:var(--text);background:var(--white)}
.page{position:relative;width:1200px;height:3348px;overflow:hidden}
.abs{position:absolute}

/* header */
.header{left:0;top:0;width:1200px;height:120px;background:var(--white)}
.brand{left:86px;top:40px;display:flex;align-items:center;gap:14px}
.brand-dot{width:40px;height:40px;border-radius:50%;background:var(--blue)}
.brand-name{font-size:42px;font-weight:400;color:var(--blue);letter-spacing:1px;line-height:42px}
.nav-item{top:66px;width:160px;margin-left:-80px;text-align:center;font-size:15px;font-weight:700;color:var(--blue);letter-spacing:.6px}

/* hero */
.hero{left:0;top:120px;width:1200px;height:555px;
  background:radial-gradient(ellipse at 50% 45%,#5E93BE 0%,#2F6596 45%,#1D4876 100%)}
.hero-title{left:300px;top:250px;width:600px;text-align:center;color:var(--white);font-size:52px;font-weight:700;line-height:61px}
.hero-text{left:390px;top:460px;width:420px;text-align:center;color:var(--white);font-size:16px;line-height:20px}

/* sections */
.section-title{left:0;width:1200px;text-align:center;font-size:38px;font-weight:700;letter-spacing:1px;color:var(--blue)}
.company{left:0;top:675px;width:1200px;height:777px;background:linear-gradient(180deg,#E4F0FD 0%,var(--light-blue) 60%,#F1F7FE 100%)}
.lead{left:290px;width:620px;text-align:center;font-size:22px;line-height:26px;color:var(--blue)}

.card{top:1027px;width:198px;height:345px;background:rgba(255,255,255,.75);padding:84px 18px 0 18px}
.portrait{top:971px;width:130px;height:115px;clip-path:polygon(25% 0,75% 0,100% 50%,75% 100%,25% 100%,0 50%);
  background:linear-gradient(160deg,#B9BEC4,#6E747B)}
.card-name{font-size:15.5px;font-weight:700;color:var(--red);line-height:19px}
.card-role{font-size:11px;font-weight:700;color:var(--red);line-height:14px;margin-bottom:16px}
.card-text{font-size:10.8px;line-height:15.6px;color:var(--text)}
.card-text+.card-text{margin-top:14px}
.card-degree{font-weight:700;color:#34404F}
.card-list{list-style:none;font-size:10.8px;line-height:15.6px}
.card-list li{padding-left:10px;text-indent:-10px}
.card-list li::before{content:"• "}

/* technology */
.technology{left:0;top:1452px;width:1200px;height:758px;background:var(--blue);overflow:hidden}
.technology .section-title{color:var(--white);top:52px}
.slide{top:160px;width:820px;height:459px;background:var(--white);overflow:hidden}
.slide--side{opacity:.35}
.slide-title{position:absolute;left:32px;top:22px;font-size:19px;font-weight:700;color:var(--blue)}
.band{position:absolute;top:66px;width:410px;height:33px;line-height:33px;text-align:center;color:var(--white);font-weight:700;font-size:15.5px}
.band--c1{left:0;background:var(--green)}
.band--c2{left:410px;background:var(--orange)}
.zone{position:absolute;top:99px;width:410px;height:360px}
.zone--c1{left:0;background:var(--light-green)}
.zone--c2{left:410px;background:var(--light-orange)}
.disease{position:absolute;font-size:15.5px;line-height:18px}
.disease ul{list-style:none;font-size:11.5px;line-height:16.5px;margin-top:1px}
.disease li{padding-left:14px;text-indent:-14px}
.disease li::before{content:"•\00a0\00a0\00a0"}
.disease--c1{color:var(--green)}
.disease--c2{color:var(--orange)}
.figure{position:absolute;left:351px;top:165px;width:120px;height:287px;border-radius:60px 60px 14px 14px;background:linear-gradient(180deg,#C9D6E4,#A9BDD3)}
.slide-links{position:absolute;left:0;top:0}
.arrow{top:1818px}
.caption{left:190px;top:2100px;width:530px;font-size:11px;line-height:15.6px;color:var(--white)}

.lab-band{left:0;top:2210px;width:1200px;height:263px;background:linear-gradient(90deg,#2A5C8E 0%,#5E8FB8 40%,#AFC3D3 75%,#8E9CAA 100%)}

/* pipeline */
.pipeline{left:0;top:2473px;width:1200px;height:556px;background:linear-gradient(180deg,#F7FAFD,#FBFCFE)}
.column{top:2737px;width:380px;font-size:13px;line-height:22px;color:var(--blue)}

/* contact */
.contact{left:0;top:3029px;width:1200px;height:319px;background:var(--blue)}
.contact .section-title{color:var(--white);top:68px}
.address{left:86px;top:3213px;font-size:18px;line-height:23px;color:var(--white)}
.map{left:796px;top:3120px;width:309px;height:195px;background:rgba(255,255,255,.95);border-radius:40% 30% 35% 45%}
.pin{left:878px;top:3072px}
</style>
</head>
<body>
<div class="page">

  <header class="abs header">
    <div class="abs brand"><span class="brand-dot"></span><span class="brand-name">velunor</span></div>
    <nav>
      <span class="abs nav-item" style="left:680px">COMPANY</span>
      <span class="abs nav-item" style="left:824px">TECHNOLOGY</span>
      <span class="abs nav-item" style="left:955px">PIPELIN</span>
      <span class="abs nav-item" style="left:1076px">KONTAKT</span>
    </nav>
  </header>

  <section class="abs hero" role="img" aria-label="Laboratory photo with glass test tubes, molecule models and chemical structure lines in blue tones"></section>
  <h1 class="abs hero-title">Unleashing the therapeutic potential of mTOR inhibition</h1>
  <p class="abs hero-text">Lorem ipsum dolor sit amet, consectetuer adipiscing elit. Aenean commodo ligula eget dolor. Aenean massa. Cum sociis natoque penatibus et magnis dis parturient montes, nascetur ridiculus</p>

  <section class="abs company"></section>
  <h2 class="abs section-title" style="top:730px">COMPANY</h2>
  <p class="abs lead" style="top:798px">Lorem ipsum dolor sit gula adipiscing elit. Aenean commodo ligula eget dolossa. Cum sociis namet, consectetuer adipiscing elit. Aenean commodo ligula adipiscing elit. Aenean commodo ligula eget dolossa.</p>

  <article class="abs card" style="left:86px">
    <p class="card-name">Dr. Jonas Wehrli,</p>
    <p class="card-role">CEO</p>
    <p class="card-text">Expert in the field of mTOR biology with 10 years of experience. (Co-)Author of breakthrough publications of the structures of human mTOR complex 1 and mTOR complex 2 in the laboratory of Prof. Lukas Ferber.</p>
    <p class="card-text card-degree">PhD in Structural Biology from the University of Lindenau.</p>
  </article>
  <article class="abs card" style="left:294px">
    <p class="card-name">Dr. Arben Kola,</p>
    <p class="card-role">Head of Biology</p>
    <p class="card-text">Expert in the field of mTOR biology. Profound knowledge on mTOR signaling acquired during his PostDoc in the laboratory of Prof. Peter K. Brandt.</p>
    <p class="card-text card-degree">PhD in Biochemistry from the University of Lakeport.</p>
  </article>
  <article class="abs card" style="left:501px">
    <p class="card-name">Dr. Rainer Holtzmann,</p>
    <p class="card-role">Medicinal Chemistry</p>
    <p class="card-text">Over 35 years of experience on preclinical research and medicinal chemistry in the areas of cardiovascular, metabolic, infectious, in-flammatory diseases, and immuno-oncology (Corvanta). Over 100 patents and publications.</p>
    <p class="card-text card-degree">PhD in Organic Chemistry from Technical University of Halden.</p>
  </article>
  <article class="abs card" style="left:709px">
    <p class="card-name">Prof. Peter K. Brandt</p>
    <p class="card-role">Group Leader at the University of Lindenau</p>
    <ul class="card-list"><li>Discovery of TOR in 1991</li><li>Key opinion leader in the TOR field</li></ul>
  </article>
  <article class="abs card" style="left:917px">
    <p class="card-name">Prof. Lukas Ferber</p>
    <p class="card-role">Group Leader at the University of Lindenau</p>
    <ul class="card-list"><li>First cryo-EM structures of mTOR complexes</li><li>Pioneer in mTOR structural biology</li></ul>
  </article>

  <div class="abs portrait" style="left:120px" role="img" aria-label="Portrait photo of Jonas Wehrli"></div>
  <div class="abs portrait" style="left:328px" role="img" aria-label="Portrait photo of Arben Kola"></div>
  <div class="abs portrait" style="left:535px" role="img" aria-label="Portrait photo of Rainer Holtzmann"></div>
  <div class="abs portrait" style="left:743px" role="img" aria-label="Portrait photo of Peter K. Brandt"></div>
  <div class="abs portrait" style="left:951px" role="img" aria-label="Portrait photo of Lukas Ferber"></div>

  <section class="abs technology">
    <h2 class="abs section-title">TECHNOLOGY</h2>

    <div class="abs slide slide--side" style="left:-640px" aria-hidden="true">
      <p class="slide-title">mTOR complex 1 and mTOR complex 2 are broadly implicated in disease</p>
      <div class="band band--c1">mTOR complex 1-associated</div><div class="band band--c2">mTOR complex 2-associated</div>
      <div class="zone zone--c1"></div><div class="zone zone--c2"></div>
    </div>
    <div class="abs slide slide--side" style="left:1020px" aria-hidden="true">
      <p class="slide-title">mTOR complex 1 and mTOR complex 2 are broadly implicated in disease</p>
      <div class="band band--c1">mTOR complex 1-associated</div><div class="band band--c2">mTOR complex 2-associated</div>
      <div class="zone zone--c1"></div><div class="zone zone--c2"></div>
      <div class="disease disease--c1" style="left:86px;top:126px">mTORopathies<ul><li>Malformations of cortical development (MCD)</li><li>Focal cortical dysplasia (FCD)</li><li>Hemimegalencephaly (HME)</li></ul></div>
      <div class="disease disease--c1" style="left:86px;top:230px">Tuberous sclerosis (TSC)<ul><li>Neurological symptoms</li><li>Benign tumors</li></ul></div>
      <div class="disease disease--c1" style="left:86px;top:334px">Cancer<ul><li>Advanced kidney cancer</li><li>Pancreatic cancer</li></ul></div>
    </div>

    <div class="abs slide" style="left:190px">
      <p class="slide-title">mTOR complex 1 and mTOR complex 2 are broadly implicated in disease</p>
      <div class="band band--c1">mTOR complex 1-associated</div>
      <div class="band band--c2">mTOR complex 2-associated</div>
      <div class="zone zone--c1"></div>
      <div class="zone zone--c2"></div>
      <svg class="slide-links" width="820" height="459" viewBox="0 0 820 459" fill="none" stroke="#7D8C9C" stroke-width="1" stroke-dasharray="2 3">
        <path d="M285 121V199M285 213V268M285 328V377"/>
        <path d="M285 156H410V170M285 240H360M285 350H345"/>
        <rect x="341" y="186" width="139" height="263"/>
        <path d="M534 143V177M534 335V377M534 156H420M534 350H480"/>
      </svg>
      <div class="figure" role="img" aria-label="Outline illustration of a human body with organs highlighted"></div>
      <div class="disease disease--c1" style="left:86px;top:118px">mTORopathies<ul><li>Malformations of cortical development (MCD)</li><li>Focal cortical dysplasia (FCD)</li><li>Hemimegalencephaly (HME)</li></ul></div>
      <div class="disease disease--c1" style="left:86px;top:222px">Tuberous sclerosis (TSC)<ul><li>Neurological symptoms</li><li>Benign tumors</li></ul></div>
      <div class="disease disease--c1" style="left:86px;top:326px">Cancer<ul><li>Advanced kidney cancer</li><li>Pancreatic cancer</li></ul></div>
      <div class="disease disease--c2" style="left:546px;top:142px">Cancer (CNS)<ul><li>Glioblastoma</li></ul></div>
      <div class="disease disease--c2" style="left:546px;top:330px">Cancer<ul><li>Bladder cancer</li><li>Breast cancer</li></ul></div>
    </div>
  </section>

  <svg class="abs arrow" style="left:86px" width="46" height="46" viewBox="0 0 46 46" aria-label="Previous slide"><circle cx="23" cy="23" r="21.5" fill="rgba(255,255,255,.15)" stroke="#fff" stroke-width="2"/><path d="M28 14L16 23L28 32Z" fill="#fff"/></svg>
  <svg class="abs arrow" style="left:1066px" width="46" height="46" viewBox="0 0 46 46" aria-label="Next slide"><circle cx="23" cy="23" r="21.5" fill="rgba(255,255,255,.15)" stroke="#fff" stroke-width="2"/><path d="M18 14L30 23L18 32Z" fill="#fff"/></svg>
  <p class="abs caption">Lorem ipsum dolor sit amet, consectetuer adipiscing elit. Aenean commodo ligula eget dolor. Aenean massa. Cum sociis natoque penatibus et magnis dis parturient montes, nascetur ridiculus mus. Donec quam felis, ultricies nec, pellentesque eu, pretium quis, sem.</p>

  <div class="abs lab-band" role="img" aria-label="Laboratory photo of a microscope and measuring scale in blue and grey tones"></div>

  <section class="abs pipeline"></section>
  <h2 class="abs section-title" style="top:2538px">PIPELINE</h2>
  <p class="abs lead" style="top:2606px;left:340px;width:520px">Lorem ipsum dolor sit amet, consectetuer adipiscing elit. Aenean commodo ligula eget dolor. Aenean massa. Cum sociis natoque penatibu.</p>
  <p class="abs column" style="left:190px">Lorem ipsum dolor sit amet, consectetuer adipiscing elit. Aenean commodo ligula eget dolor. Aenean massa. Cum sociis natoque penatibus et magnis dis parturient montes, nascetur ridiculus mus. Donec quam felis, ultricies nec, pellentesque eu, pretium quis, sem. Nulla consequat massa quis enim. Donec pede justo, fringilla vel, aliquet nec, vulputate eget, arcu. In enim justo, rhoncus ut, imperdiet a, venenatis vitae, justo. Nullam dictum felis eu pede mollis pretium. Integer tincidunt. Cras dapibus. Vivamus elementum</p>
  <p class="abs column" style="left:634px">Lorem ipsum dolor sit amet, consectetuer adipiscing elit. Aenean commodo ligula eget dolor. Aenean massa. Cum sociis natoque penatibus et magnis dis parturient montes, nascetur ridiculus mus. Donec quam felis, ultricies nec, pellentesque eu, pretium quis, sem. Nulla consequat massa quis enim. Donec pede justo, fringilla vel, aliquet nec, vulputate eget, arcu. In enim justo, rhoncus ut, imperdiet a, venenatis vitae, justo. Nullam dictum felis eu pede mollis pretium. Integer tincidunt. Cras dapibus. Vivamus elementum</p>

  <section class="abs contact">
    <h2 class="abs section-title">KONTAKT</h2>
  </section>
  <address class="abs address" style="font-style:normal">Velunor Therapeutics GmbH<br>c/o Lifecentre, University of Lindenau Talweg 18<br>4810 Lindenau</address>
  <div class="abs map" role="img" aria-label="Map of Switzerland showing the company location"></div>
  <svg class="abs pin" width="54" height="68" viewBox="0 0 54 68" aria-label="Location pin"><path d="M27 2C13 2 2 13 2 27C2 45 27 66 27 66C27 66 52 45 52 27C52 13 41 2 27 2Z" fill="var(--red)"/><circle cx="27" cy="26" r="9" fill="#fff"/></svg>

</div>
</body>
</html>
```